Ardenwell Building and Property Services needs a business card design

We need a business card design for our building and property services business. We already have a logo we just need a creative design and layout on a business card. Emphasis on clean, modern, professional.
Our client targets are mainly body corporates, building managers, construction managers.
We are a building services company that lean more to structural repair of buildings, through concrete rectification and carbon fibre strengthening.
We also refurbish facades, rendering, painting etc
We target higher end body corporates in prestigious locations, hence why we'd like our cards to reflect professionalism, strength, efficiency

Target Market(s)

body corporates, building managers, construction managers

Industry/Entity Type

Construction

Contact Information for Business Card

Ardenwell is the main word, with 'Building and Property Services' underneath.
Level 17, 82 Harlow Street
MERRIDALE
Melbourne
Vic 3094
T: 9518 2736
Duncan Ferris - Director
dunardenwell@mailbox-example.com

Requirements
Must have
• Stand out on the back of the card- strong/ bold, company logo
• All of the contact details written above
Should not have
• I'd like the card to stand out, especially on the back. Id like the company logo to be prominent, although feel free to be creative around it. But remain clean and professional

```html
<!DOCTYPE html>
<html lang="en">
<head>
<meta charset="utf-8">
<title>Ardenwell Building and Property Services – Business Card</title>
<link href="https://fonts.googleapis.com/css2?family=Open+Sans:wght@400;600;700&display=swap" rel="stylesheet">
<style>
  :root {
    --page-bg: #ececec;
    --card-white: #ffffff;
    --brand-blue: #1a7fd0;
    --brand-deep: #00539c;
    --brand-glow: #2fa3e6;
    --text-grey: #6b6b6b;
    --tagline-grey: #7a7a7a;
  }
  * { margin: 0; padding: 0; box-sizing: border-box; }
  html, body {
    width: 1200px; height: 1200px; overflow: hidden;
    background: var(--page-bg);
    font-family: "Open Sans", Arial, sans-serif;
  }
  .sheet {
    width: 1200px; height: 1200px;
    display: flex; flex-direction: column; align-items: center; justify-content: center;
    gap: 60px;
  }
  .card {
    width: 880px; height: 503px;
    position: relative;
    box-shadow: 0 6px 24px rgba(0,0,0,0.12);
  }
  .card-front { background: var(--card-white); }
  .card-back {
    background: radial-gradient(circle at 50% 50%, var(--brand-glow) 0%, #1378c4 30%, var(--brand-deep) 70%);
    display: flex; align-items: center; justify-content: center;
  }

  .wordmark {
    position: absolute; left: 64px; top: 200px;
    display: flex; flex-direction: column; align-items: flex-start;
  }
  .wordmark-row { display: flex; align-items: center; gap: 14px; }
  .wordmark-square { width: 30px; height: 30px; background: var(--brand-blue); }
  .wordmark-name {
    font-size: 46px; font-weight: 600; color: var(--brand-blue);
    letter-spacing: 3px; text-transform: uppercase; line-height: 1;
  }
  .wordmark-tagline {
    margin-top: 10px; margin-left: 44px;
    font-size: 12.5px; font-weight: 600; color: var(--tagline-grey);
    letter-spacing: 2px; text-transform: uppercase;
  }

  .contact {
    position: absolute; left: 480px; top: 150px;
    color: var(--text-grey);
  }
  .contact-name { font-size: 28px; font-weight: 700; color: var(--brand-blue); line-height: 1.2; }
  .contact-role { font-size: 19px; margin-bottom: 26px; }
  .contact-address { font-size: 19px; line-height: 1.5; margin-bottom: 20px; }
  .contact-line { display: flex; align-items: center; gap: 12px; font-size: 19px; line-height: 1.7; }
  .contact-line svg { width: 20px; height: 20px; flex: none; }

  .back-mark { display: flex; align-items: center; gap: 18px; }
  .back-square { width: 44px; height: 44px; background: #ffffff; }
  .back-name {
    font-size: 64px; font-weight: 600; color: #ffffff;
    letter-spacing: 5px; text-transform: uppercase; line-height: 1;
  }
</style>
</head>
<body>
<main class="sheet">
  <section class="card card-front" aria-label="Business card front">
    <div class="wordmark">
      <div class="wordmark-row">
        <span class="wordmark-square"></span>
        <span class="wordmark-name">Ardenwell</span>
      </div>
      <span class="wordmark-tagline">Building and Property Services</span>
    </div>

    <div class="contact">
      <p class="contact-name">Duncan Ferris</p>
      <p class="contact-role">Director</p>
      <p class="contact-address">Level 17, 82 Harlow Street<br>MERRIDALE Melbourne&nbsp; Vic 3094</p>
      <p class="contact-line">
        <svg viewBox="0 0 24 24" aria-hidden="true"><path fill="#1a7fd0" d="M6.6 10.8a15.1 15.1 0 0 0 6.6 6.6l2.2-2.2c.3-.3.7-.4 1-.2 1.1.4 2.3.6 3.6.6.6 0 1 .4 1 1V20c0 .6-.4 1-1 1A17 17 0 0 1 3 4c0-.6.4-1 1-1h3.5c.6 0 1 .4 1 1 0 1.3.2 2.5.6 3.6.1.3 0 .7-.2 1z"/></svg>
        <span>9518 2736</span>
      </p>
      <p class="contact-line">
        <svg viewBox="0 0 24 24" aria-hidden="true"><rect x="2" y="5" width="20" height="14" fill="#1a7fd0"/><path d="M2 5l10 8 10-8" fill="none" stroke="#ffffff" stroke-width="1.6"/></svg>
        <span>dunardenwell@mailbox-example.com</span>
      </p>
    </div>
  </section>

  <section class="card card-back" aria-label="Business card back">
    <div class="back-mark">
      <span class="back-square"></span>
      <span class="back-name">Ardenwell</span>
    </div>
  </section>
</main>
</body>
</html>
```